logo needed for Registered Massage Therapy cards, banner, flyers and wesbite

Solace Wellness is a Registered Massage Therapy clinic.
We offer clinic massage, event massage, work place massage and home visits for treatment and relaxation.

I picked Solace because of the meaning behind the word. I want clients to know we go above and beyond the expectations of Registered Massage Therapy and they should recognise that from our client care, our clinic and personal presentation and our media representation.

The company is based in Ontario and the clinic is in a health awareness plaza which includes Yoga, Iron Pulse gym and Children's gyms.

The logo must appeal to the general public and to Marketing and Business's. The logo should be calming, have a nice flow, be clean and inspiring.

I have played with some designs myself which you are free to look at in my portfolio. I am including a hand image that I like, though I do not like the colour and the swirly image that is inside the hand which i'd like to incorporate behind the 2 letter T's so that I may use the "S W" abbreviation as a logo on a t shirt.

We do not have to use the images I have submitted but I like the idea of using a hand with the swirls that look something like something growing and living. I would like as I said my image to be worked into the T's of the logo.

Reason: I am opening my business on July 14th and must submit a logo to my banner and sign company a minimum of 10 days before this date. Thank you !

THESE ARE THE COLOURS BEING USED IN THE RECEPTION OF THE CLINIC.

THE LOGO WOULD BE DISPLAYED ON THE CHINCHILLA COLOURED WALL.
CAN WE USE THESE COLOURS OR COLOURS SIMILAR FOR THE LOGO?

Target Market(s)

Health, Professional, Mother, Male and Female,

Industry/Entity Type

Massage

Contact Information for Business Card

Solace Wellness
REGISTERED MASSAGE THERAPY
** Each individual Therapists name and the business telephone number and website will appear under the logo which I can enter in for each therapist as I need to **

Logo Text

Solace Wellness Registered Massage Therapy

Requirements
Must have
• Solace Wellness should be clearly the business name, nicely spaced.
Registered Massage Therapy should appear underneath to show what the business is. The lettering should not appear harsh. It should have a slight flow to it and a slight softness. The viewer should think "zen and calm and clean and professional" when they see the logo. The colours must work well together and tie into the logo image/images. I like using one colour for the business name and then having some kind of block box or swirl box underneath containing the Registered Massage Therapy written in white to contrast with the business name.
Nice to have
• Solace means grow or go above and beyond, the image and S and W should give this feeling.

```html
<!DOCTYPE html>
<html lang="en">
<head>
<meta charset="utf-8">
<title>Solace Wellness – Business Card</title>
<link rel="stylesheet" href="https://fonts.googleapis.com/css2?family=Cinzel:wght@700&family=Comfortaa:wght@400&family=Lato:wght@400&family=Poiret+One&display=swap">
<style>
  :root {
    --card-cream: #f1f4e1;
    --ink-grey: #6e6e6e;
    --ink-dark: #4a4a4a;
    --name-grey: #5a5a5a;
    --sage: #a8b9a3;
    --sage-soft: #c9d5c3;
    --band-top: #a3b2a1;
    --band-bottom: #5d6a5e;
  }
  html, body {
    margin: 0;
    padding: 0;
    overflow: hidden;
    background: var(--card-cream);
  }
  .card {
    position: relative;
    width: 1200px;
    height: 695px;
    background: var(--card-cream);
    overflow: hidden;
  }
  .therapist-name {
    position: absolute;
    top: 46px;
    right: 62px;
    margin: 0;
    font-family: "Cinzel", serif;
    font-weight: 700;
    font-size: 36px;
    letter-spacing: 1px;
    color: var(--name-grey);
  }
  .monogram {
    position: absolute;
    left: 446px;
    top: 78px;
    width: 352px;
    height: 262px;
    display: flex;
    align-items: center;
    justify-content: center;
    gap: 28px;
  }
  .monogram-letter {
    font-family: "Poiret One", sans-serif;
    font-size: 230px;
    line-height: 1;
    color: var(--ink-grey);
  }
  .monogram-dot {
    width: 54px;
    height: 54px;
    border-radius: 50%;
    background: var(--sage-soft);
  }
  .business-name {
    position: absolute;
    left: 0;
    width: 100%;
    top: 338px;
    margin: 0;
    text-align: center;
    font-family: "Poiret One", sans-serif;
    font-weight: 400;
    font-size: 96px;
    line-height: 1;
    color: var(--ink-grey);
  }
  .service-line {
    position: absolute;
    left: 0;
    width: 100%;
    top: 440px;
    margin: 0;
    text-align: center;
    font-family: "Comfortaa", sans-serif;
    font-size: 46px;
    line-height: 1;
    color: var(--sage);
  }
  .phone {
    position: absolute;
    left: 0;
    width: 100%;
    top: 512px;
    margin: 0;
    text-align: center;
    font-family: "Lato", sans-serif;
    font-size: 40px;
    letter-spacing: 1px;
    color: var(--ink-dark);
  }
  .website {
    position: absolute;
    left: 0;
    width: 100%;
    top: 565px;
    margin: 0;
    text-align: center;
    font-family: "Lato", sans-serif;
    font-size: 35px;
    color: var(--ink-grey);
  }
  .footer-band {
    position: absolute;
    left: 0;
    bottom: 0;
    width: 100%;
    height: 66px;
    background: linear-gradient(to bottom, var(--band-top), var(--band-bottom));
  }
</style>
</head>
<body>
  <main class="card">
    <p class="therapist-name">Mara Ellison</p>

    <div class="monogram" aria-label="S W">
      <span class="monogram-letter">S</span>
      <span class="monogram-dot"></span>
      <span class="monogram-letter">W</span>
    </div>

    <h1 class="business-name">Solace Wellness</h1>
    <p class="service-line">registered massage therapy</p>

    <p class="phone">027 555 0142</p>
    <p class="website">www.solacewellnessrmt.com.au</p>

    <div class="footer-band"></div>
  </main>
</body>
</html>
```